Exciting letterhead design for startup company

We need a A4 letterhead designing.

See attached file which contains the logo (on 3 different coloured backgrounds) and then the address and contact information. It also contains 4 colours that can be used.

Looking for an imaginative design. We are a young, fresh startup website design company so need a letterhead that reflects our industry.

Font styles to use
Sans Serif

```html
<!DOCTYPE html>
<html lang="en">
<head>
<meta charset="utf-8">
<title>PixelNest Letterhead</title>
<link href="https://fonts.googleapis.com/css2?family=Questrial&family=Roboto+Condensed:wght@400&display=swap" rel="stylesheet">
<style>
  :root {
    --bg: #e4e5e6;
    --paper: #f7f7f7;
    --charcoal: #434749;
    --green: #6cb24a;
    --ink: #505457;
    --sig-blue: #c9d2e6;
    --footer-text: #d8dadb;
  }
  * { box-sizing: border-box; margin: 0; padding: 0; }
  html, body {
    width: 1200px; height: 968px; overflow: hidden;
    background: var(--bg);
  }
  .letterhead {
    position: absolute; left: 268px; top: 14px;
    width: 664px; height: 940px;
    background: var(--paper);
    box-shadow: 0 2px 10px rgba(0,0,0,0.12);
    font-family: "Questrial", sans-serif;
    color: var(--ink);
  }
  .header-band {
    position: absolute; left: 0; top: 0; width: 100%; height: 72px;
    background: var(--charcoal);
    border-bottom: 4px solid var(--green);
  }
  .brand-box {
    position: absolute; left: 206px; top: 22px;
    width: 168px; height: 82px;
    background: var(--charcoal);
    border: 4px solid var(--green);
    border-top: none;
    display: flex; align-items: center; justify-content: center;
  }
  .brand-name {
    font-family: "Questrial", sans-serif;
    font-size: 27px; color: #ffffff; letter-spacing: 0.5px;
  }
  .fold-mark {
    position: absolute; left: 0; width: 14px; height: 1px; background: #c4c6c8;
  }
  .fold-mark.upper { top: 313px; }
  .fold-mark.lower { top: 626px; }
  .letter-body {
    position: absolute; left: 72px; top: 188px; width: 520px;
    font-size: 9.6px; line-height: 1.5;
  }
  .letter-body p { margin-bottom: 9px; font-style: italic; }
  .salutation { font-weight: bold; font-style: normal !important; margin-bottom: 8px !important; }
  .sign-off { font-style: italic; }
  .signatory { font-weight: bold; font-style: italic; }
  .signature {
    display: block; width: 120px; height: 44px; margin-top: 6px;
    background: linear-gradient(90deg, var(--sig-blue), #e7ebf3);
    border-radius: 3px;
  }
  .footer-band {
    position: absolute; left: 0; bottom: 0; width: 100%; height: 46px;
    background: var(--charcoal);
    border-top: 4px solid var(--green);
    display: flex; align-items: center; gap: 22px;
    padding: 0 26px;
    font-family: "Roboto Condensed", sans-serif;
    font-size: 11px; color: var(--footer-text);
  }
  .footer-band .address { margin-right: auto; }
  .contact-item { display: flex; align-items: center; gap: 6px; }
  .contact-icon { width: 13px; height: 13px; flex: none; }
</style>
</head>
<body>
  <div class="letterhead">
    <div class="header-band"></div>
    <div class="brand-box"><span class="brand-name">PixelNest</span></div>

    <span class="fold-mark upper"></span>
    <span class="fold-mark lower"></span>

    <div class="letter-body">
      <p class="salutation">Dear sir,</p>
      <p>Communication is a very integral part of living creatures, animals and humans. Communication may be verbal or written. Written communication, however is only applicable to human beings. Can you even imagine a world without communication? Verbal communication can be through telephones, webcams or in person. Written communication is through letters, emails and mobile phone messages.</p>
      <p>In today's world of great inventions and technology, letters have somehow become redundant. It is the time for text messages or chats. But they still can communicate a lot more than all other modes of communication. Organizations and various government departments still bank on letters as a strong medium of communication. There is no comparison in costs of sending letters as compared to costs of mobile phone messages though &ndash; letters are far cheaper. Letters now commonly known as &ldquo;hard copy documents&rdquo; are considered more relevant and important than email copies or text messages as proof or evidence of some sort.</p>
      <p>Letters speak volumes about a person or an organization that writes it. So one must take utmost care ensuring that the language used in any letter is appropriate for the occasion for which it is being written. Since a letter is also a written proof or document, if there are certain things that should not form a part of it, then that too should be carefully handled.</p>
      <p>Writing a good letter is an art. But if for some reason someone is unable to write that perfect letter, these different types of letters provide a base for you to build on. Sample letters have been given for everyone to understand what all information needs to form a part of the letter type and then it can be customized.</p>
      <p class="sign-off">Yours Sincerely,<br><span class="signatory">Dana Whitfield</span></p>
      <span class="signature" role="img" aria-label="Handwritten signature of Dana Whitfield"></span>
    </div>

    <div class="footer-band">
      <span class="address">Unit 4, Harbour Court, Canal Road, Leeds, LS12 3QX, United Kingdom</span>
      <span class="contact-item">
        <svg class="contact-icon" viewBox="0 0 13 13" aria-hidden="true">
          <rect width="13" height="13" rx="2" fill="#3b8fd4"/>
          <path d="M4 3.2c.4-.3.8-.3 1 .1l.7 1.3c.2.3.1.6-.2.8l-.4.3c.4.9 1.1 1.6 2 2l.3-.4c.2-.3.5-.4.8-.2l1.3.7c.4.2.4.6.1 1-.5.7-1.2.9-2 .6C5.8 8.8 4.2 7.2 3.6 5.4c-.3-.8 0-1.6.4-2.2z" fill="#fff"/>
        </svg>
        0800 555 0193
      </span>
      <span class="contact-item">
        <svg class="contact-icon" viewBox="0 0 13 13" aria-hidden="true">
          <rect width="13" height="13" rx="2" fill="var(--green)"/>
          <rect x="2.5" y="4" width="8" height="5.5" fill="none" stroke="#fff" stroke-width="1"/>
          <path d="M2.5 4l4 3 4-3" fill="none" stroke="#fff" stroke-width="1"/>
        </svg>
        hello@pixelnest.co.uk
      </span>
      <span class="contact-item">
        <svg class="contact-icon" viewBox="0 0 13 13" aria-hidden="true">
          <rect width="13" height="13" rx="2" fill="#e0b62c"/>
        </svg>
        @pixelnest
      </span>
    </div>
  </div>
</body>
</html>
```